Label Wanted For New, Millennial, Hard Apple Cider Brand

California, alcoholic apple cider brand targeted towards Millennials needs a label to show product as:

Hand-crafted. Modern. Hipster. Produced from apples. Delicious. Unisex.

We are primarily a small wine producer (500cs/year - 20 barrels/year). Check the attachments for one of our current labels. Tidewhistle will be the name of our cider.

This is the first release of our cider. This cider bottle we will be using is attached (Champagne Mold with a Crown Cap).

We will have several flavors over the course of the next few years and need a placeholder on the front label for the specific style:
"Off-Dry" (Tart + a Little Sweet)
"Dry" (Crisp + Tart)
"Hopped" (Fermented with Hopps)
"HoneyBee" (Fermented with Honey)
"Barrel Aged" (Aged in Barrel)
"Cross Culture" (Fermented with Wine Yeast and Viognier), etc.

Looking for a label that is modern, but also somewhat rustic. Please view our "Labels We Like" file. Something creative and different. Definitely more on the hipster side of things than old-fashioned.
Updates

Project Deadline Extended Reason: Hi designers,We are postponing the deadline due to the holidays. We've been unable to provide effective feedback to many of you with the craziness of Christmas Eve, Christmas and now New Years! Thank you for your patience. We will have feedback for many of you tomorrow and final selections on January 02. Thank you for all of your hard work. - Noor Added Friday, December 26, 2014

Target Market(s)

26-44yr old, educated, outdoorsy, food/wine loving, beer/wine/spirit drinking adults. Unisex product - should be slightly more masculine than feminine.

Industry/Entity Type

Product

Font styles to use
Decorative

Requirements
Must have
• Front:
• 1. Front Label Measurements: Maintain a 4(w) x 4.125(h) inch front with 1/4in bleed.
• 2. Font used for brand name "Tidewhistle" should be legible but unique.
• 3. Artwork should be unisex. Modern with a handcrafted look.
• 4. Front Label Must Contain the Following Info:
• a. "Alc / Vol 7.0%"
• b. California Hard Apple Cider
• c. Placeholder for style of cider (DRY, HOPPED, OFF-DRY, etc.)
• Back Label:
• 1. Back Label Measurements: Maintain a 3(w) x 4.125(h) inch back w/ 1/4in bleed. One back label will be used for all ciders
• 2. Back Label Must Contain the Following Info:
• a. "GOVERNMENT WARNING: (1) ACCORDING TO THE SURGEON GENERAL, WOMEN SHOULD NOT DRINK ALCOHOLIC BEVERAGES DURING PREGNANCY BECAUSE OF THE RISK OF BIRTH DEFECTS. (2) CONSUMPTION OF ALCOHOLIC BEVERAGES IMPAIRS YOUR ABILITY TO DRIVE A CAR OR OPERATE MACHINERY, AND MAY CAUSE HEALTH PROBLEMS."
• b. "CONTAINS SULFITES"
• c. "Produced & Bottled by FM Vine Co, Buellton, CA".
• d. Back label copy. T
• "We Love-love cider. Call us crazy, but we feel that cider just might be the bridge between beer-only drinkers and wine-only drinkers - a white flag of sorts. Go on, shake hands. Finally something we can all agree on. Break free from the norm. Drink what you love. Cheers. Noor K."
Nice to have
• 1. OPEN THE "LABELS I LIKE" FILE. Do not submit a design before looking a this file.
• 2. Label must tie in brand name, "Tide Whistle" with a clever prison reference. Prison bars, barbed wire, a shovel, a prison shank, a spoon used to dig a tunnel, a rock pick, a pick-axe, etc.
• 3. Label must tie in apples / apple trees, etc. Something showing what our cider is made of.
• 4. Label must have a memorable font or a logo for brand recognition that will be congruent across all labels.
Should not have
• NO worms in apples please. People do not want to associate or visualize anything like that for food /beverage products.

```html
<!DOCTYPE html>
<html lang="en">
<head>
<meta charset="utf-8">
<title>Tidewhistle California Hard Apple Cider – Front Label</title>
<link rel="stylesheet" href="https://fonts.googleapis.com/css2?family=Arimo:wght@400;700&display=swap">
<style>
  :root {
    --page-bg: #ffffff;
    --label-white: #ffffff;
    --frame-red: #b3200f;
    --frame-orange: #f08a1c;
    --band-red: #a8170c;
    --band-red-dark: #8c1208;
    --orange-light: #f9a12a;
    --orange-mid: #f07a1a;
    --orange-deep: #e0541a;
    --brand-orange: #e2571c;
    --art-red: #c92a12;
    --art-amber: #f3a23a;
    --gold: #d4a24a;
    --text-white: #ffffff;
  }
  * { box-sizing: border-box; margin: 0; padding: 0; }
  html, body {
    width: 1200px;
    height: 1100px;
    overflow: hidden;
    background: var(--page-bg);
  }
  .canvas {
    position: relative;
    width: 1200px;
    height: 1100px;
  }
  .front-label {
    position: absolute;
    left: 150px;
    top: 95px;
    width: 900px;
    height: 910px;
    background: var(--label-white);
    border: 7px solid var(--frame-red);
    border-radius: 10px;
    box-shadow: inset 0 0 0 3px var(--frame-orange);
    overflow: hidden;
    font-family: "Arimo", Arial, sans-serif;
  }
  .sunrise-art {
    position: absolute;
    left: 200px;
    top: 30px;
    width: 490px;
    height: 230px;
    border-radius: 50% 50% 8px 8px / 70% 70% 8px 8px;
    background: radial-gradient(ellipse at 50% 100%, var(--art-red) 0%, var(--brand-orange) 40%, var(--art-amber) 70%, rgba(243,162,58,0) 100%);
    opacity: 0.85;
  }
  .brand-name {
    position: absolute;
    left: 0;
    right: 0;
    top: 260px;
    text-align: center;
    font-weight: 700;
    font-size: 150px;
    line-height: 1;
    letter-spacing: -2px;
    color: var(--brand-orange);
  }
  .style-band {
    position: absolute;
    left: 0;
    right: 0;
    top: 570px;
    height: 110px;
    background: linear-gradient(180deg, var(--band-red) 0%, var(--band-red-dark) 100%);
    color: var(--text-white);
    text-align: center;
    font-weight: 700;
    font-size: 38px;
    line-height: 46px;
    padding-top: 10px;
    letter-spacing: 0.5px;
  }
  .divider {
    position: absolute;
    left: 0;
    right: 0;
    top: 700px;
    height: 6px;
    background: var(--orange-light);
  }
  .base-panel {
    position: absolute;
    left: 0;
    right: 0;
    top: 712px;
    bottom: 0;
    background: linear-gradient(180deg, var(--orange-light) 0%, var(--orange-mid) 55%, var(--orange-deep) 100%);
    color: var(--text-white);
  }
  .apple-texture {
    position: absolute;
    left: 310px;
    top: 35px;
    width: 260px;
    height: 140px;
    border-radius: 45%;
    background: radial-gradient(ellipse at center, var(--gold) 0%, rgba(212,162,74,0.6) 60%, rgba(212,162,74,0) 100%);
  }
  .abv {
    position: absolute;
    left: 30px;
    top: 80px;
    font-size: 26px;
    line-height: 30px;
    font-weight: 400;
  }
  .volume {
    position: absolute;
    right: 40px;
    top: 110px;
    font-size: 28px;
    font-weight: 400;
  }
</style>
</head>
<body>
  <main class="canvas">
    <section class="front-label">
      <div class="sunrise-art" role="img" aria-label="Illustration of a mountain peak under a radiating sunrise in red and orange"></div>
      <h1 class="brand-name">Tidewhistle</h1>
      <div class="style-band">
        <p>CALIFORNIA</p>
        <p>HARD APPLE CIDER</p>
      </div>
      <div class="divider"></div>
      <div class="base-panel">
        <div class="apple-texture" role="img" aria-label="Textured gold apple tree emblem"></div>
        <p class="abv">ALC<br>VOL 7.0%</p>
        <p class="volume">75 mL</p>
      </div>
    </section>
  </main>
</body>
</html>
```